Tovin Wine Label Design Project

We are creating a wine with a winery in New Hampshire. USA. The bottles need a label Here are some specifics
Brand name Silvara XIV (latin for Grove 14)
Wine: is a blend of Cabernet Sauvignon, Merlot and Shiraz (dominant varietal is cabernet)
Vintage 2023
All ideas from here are thoughts:
Elegant serif or calligraphic script for a sophisticated look. Perhaps Gold foil or embossed for prominence.
Background suggestions: deep Burgandy or matt black for contrast
Illustrations suggestions: Roman inspired wreath (laurel) or column or stylized roman coin.
Tagline suggestion: Timeless
All these graphic elements are just suggestions, you all are the pros. have at it and good luck

```html
<!DOCTYPE html>
<html lang="en">
<head>
<meta charset="utf-8">
<title>Silvara XIV — Wine Label</title>
<link href="https://fonts.googleapis.com/css2?family=Cinzel:wght@400;600;700&display=swap" rel="stylesheet">
<style>
  :root {
    --label-black: #000000;
    --gold-light: #f7d77a;
    --gold-mid: #c9962e;
    --gold-deep: #7a4a12;
    --bronze: #5a3410;
    --coin-light: #e0b458;
    --coin-dark: #8a5d1c;
  }
  html, body {
    margin: 0;
    padding: 0;
    width: 900px;
    height: 1200px;
    overflow: hidden;
    background: var(--label-black);
  }
  .label {
    position: relative;
    width: 900px;
    height: 1200px;
    background: var(--label-black);
    overflow: hidden;
    font-family: "Cinzel", "Times New Roman", serif;
  }
  .label-frame {
    position: absolute;
    inset: 0;
  }
  .corner-flourish {
    position: absolute;
    width: 150px;
    height: 150px;
    background: radial-gradient(circle at 30% 30%, rgba(201,150,46,0.55), rgba(122,74,18,0.15) 60%, transparent 75%);
  }
  .corner-flourish.top-left { top: 40px; left: 40px; }
  .corner-flourish.top-right { top: 40px; right: 40px; transform: scaleX(-1); }
  .corner-flourish.bottom-left { bottom: 40px; left: 40px; transform: scaleY(-1); }
  .corner-flourish.bottom-right { bottom: 40px; right: 40px; transform: scale(-1,-1); }
  .coin-emblem {
    position: absolute;
    left: 208px;
    top: 130px;
    width: 470px;
    height: 470px;
    border-radius: 50%;
    background: radial-gradient(circle at 45% 40%, var(--coin-light), #b98632 55%, var(--coin-dark) 100%);
    box-shadow: inset 0 0 0 14px rgba(90,52,16,0.35);
  }
  .rule {
    position: absolute;
    left: 128px;
    width: 644px;
    height: 2px;
    background: linear-gradient(90deg, var(--gold-deep), var(--gold-mid), var(--gold-deep));
  }
  .rule.upper { top: 666px; }
  .rule.lower { top: 837px; }
  .wine-name {
    position: absolute;
    top: 690px;
    left: 0;
    width: 900px;
    margin: 0;
    text-align: center;
    font-weight: 400;
    font-size: 100px;
    line-height: 120px;
    letter-spacing: 1px;
    background: linear-gradient(180deg, var(--gold-light) 0%, #e9b93c 50%, var(--gold-deep) 100%);
    -webkit-background-clip: text;
    background-clip: text;
    color: transparent;
  }
  .tagline {
    position: absolute;
    top: 862px;
    left: 0;
    width: 900px;
    margin: 0;
    text-align: center;
    font-weight: 400;
    font-size: 48px;
    line-height: 60px;
    letter-spacing: 2px;
    background: linear-gradient(180deg, #f1c35a, var(--gold-deep));
    -webkit-background-clip: text;
    background-clip: text;
    color: transparent;
  }
  .vintage-seal {
    position: absolute;
    left: 350px;
    top: 985px;
    width: 200px;
    height: 200px;
  }
  .vintage-seal-text {
    position: absolute;
    inset: 0;
    display: flex;
    flex-direction: column;
    align-items: center;
    justify-content: center;
    color: var(--gold-mid);
  }
  .vintage-word {
    font-size: 30px;
    line-height: 34px;
    letter-spacing: 1px;
    margin-top: 6px;
  }
  .vintage-year {
    font-size: 56px;
    line-height: 60px;
    font-weight: 700;
    background: linear-gradient(180deg, var(--gold-light), var(--gold-deep));
    -webkit-background-clip: text;
    background-clip: text;
    color: transparent;
  }
</style>
</head>
<body>
  <main class="label">
    <svg class="label-frame" width="900" height="1200" viewBox="0 0 900 1200" aria-hidden="true">
      <defs>
        <linearGradient id="frameGold" x1="0" y1="0" x2="0" y2="1">
          <stop offset="0" stop-color="#7a4a12"/>
          <stop offset="0.5" stop-color="#e8c35a"/>
          <stop offset="1" stop-color="#7a4a12"/>
        </linearGradient>
      </defs>
      <rect class="key-band" x="20" y="20" width="860" height="1160" fill="none" stroke="url(#frameGold)" stroke-width="40" role="img" aria-label="Greek key meander border band"/>
      <rect class="inner-line" x="46" y="46" width="808" height="1108" fill="none" stroke="#c9962e" stroke-width="2"/>
    </svg>

    <div class="corner-flourish top-left" role="img" aria-label="Gold scroll flourish ornament"></div>
    <div class="corner-flourish top-right" role="img" aria-label="Gold scroll flourish ornament"></div>
    <div class="corner-flourish bottom-left" role="img" aria-label="Gold scroll flourish ornament"></div>
    <div class="corner-flourish bottom-right" role="img" aria-label="Gold scroll flourish ornament"></div>

    <div class="coin-emblem" role="img" aria-label="Antique Roman gold coin with laureate profile"></div>

    <div class="rule upper"></div>
    <h1 class="wine-name">SILVARA XIV</h1>
    <div class="rule lower"></div>
    <p class="tagline">TIMELESS</p>

    <div class="vintage-seal">
      <svg width="200" height="200" viewBox="0 0 200 200" aria-hidden="true">
        <defs>
          <radialGradient id="sealRing" cx="0.5" cy="0.4" r="0.6">
            <stop offset="0" stop-color="#e8c35a"/>
            <stop offset="1" stop-color="#6b3f10"/>
          </radialGradient>
        </defs>
        <circle cx="100" cy="100" r="98" fill="#000"/>
        <circle cx="100" cy="100" r="96" fill="none" stroke="#c9962e" stroke-width="3"/>
        <circle cx="100" cy="100" r="84" fill="none" stroke="url(#sealRing)" stroke-width="16" role="img" aria-label="Greek key ring pattern"/>
        <circle cx="100" cy="100" r="74" fill="#000" stroke="#c9962e" stroke-width="2"/>
      </svg>
      <div class="vintage-seal-text">
        <span class="vintage-word">VINTAGE</span>
        <span class="vintage-year">2023</span>
      </div>
    </div>
  </main>
</body>
</html>
```